Pediatric Dental Practice needs a postcard for direct mail advertising

We are looking for a creative and professional double-sided postcard design for a direct mail marketing campaign. Our goal is to attract new families to our pediatric dental practice by conveying a sense of warmth, modern care, and clinical excellence. The design should feel "boutique" and high-end yet remain fun and approachable for parents and children.

```html
<!DOCTYPE html>
<html lang="en">
<head>
<meta charset="utf-8">
<title>Maple Grove Pediatric Dentistry – Postcard</title>
<link href="https://fonts.googleapis.com/css2?family=Outfit:wght@300;400;500;600&family=Playfair+Display:wght@700&display=swap" rel="stylesheet">
<style>
  :root {
    --backdrop: #4a4a4a;
    --card: #ffffff;
    --mint-top: #ffffff;
    --mint-bottom: #d3ecd4;
    --green: #4fb86c;
    --green-deep: #2f9a57;
    --pill: #c2ebc1;
    --pill-end: #a7dea9;
    --ink: #2a2a2a;
    --ink-soft: #3c3c3c;
    --line: #cfe8cf;
    --stamp-line: #cfcfcf;
    --smile-dark: #2a2a2a;
    --smile-light: #e9eff3;
  }
  * { box-sizing: border-box; margin: 0; padding: 0; }
  html, body { width: 926px; height: 1200px; overflow: hidden; }
  body { background: var(--backdrop); font-family: "Outfit", sans-serif; color: var(--ink); position: relative; }

  .card { position: absolute; left: 74px; width: 778px; height: 518px; background: var(--card); overflow: hidden; }
  .card--front { top: 67px; background: linear-gradient(180deg, var(--mint-top) 0%, #eaf6ea 45%, var(--mint-bottom) 100%); }
  .card--back { top: 614px; }
  .card > * { z-index: 2; }

  /* front */
  .brand { position: absolute; top: 44px; left: 0; width: 100%; text-align: center; }
  .brand__row { display: inline-flex; align-items: center; gap: 10px; }
  .brand__dot { width: 22px; height: 22px; border-radius: 50%; background: var(--green); }
  .brand__name { font-weight: 500; font-size: 26px; letter-spacing: 0.5px; color: var(--ink); }
  .brand__sub { font-weight: 500; font-size: 9px; letter-spacing: 3px; color: var(--ink); margin-top: 2px; }

  .headline { position: absolute; top: 162px; left: 0; width: 100%; text-align: center; font-family: "Playfair Display", serif; font-weight: 700; font-size: 66px; line-height: 1; color: var(--green); letter-spacing: -1px; }
  .subhead { position: absolute; top: 258px; left: 203px; font-size: 37px; line-height: 44px; font-weight: 400; color: var(--ink); letter-spacing: -0.5px; }

  .smile-art { position: absolute; z-index: 1; left: 40px; top: 306px; width: 390px; height: 200px;
    border-radius: 6% 6% 50% 50% / 10% 10% 90% 90%;
    background: radial-gradient(ellipse at 50% 30%, var(--smile-light) 0%, #c9d6df 45%, var(--smile-dark) 78%); }

  .tag-pill { position: absolute; left: 429px; top: 330px; width: 284px; height: 61px; border-radius: 30px; background: linear-gradient(90deg, var(--pill), var(--pill-end)); border: 2px solid #fff; display: flex; align-items: center; padding-left: 22px; font-size: 26px; font-weight: 400; color: var(--ink); letter-spacing: -0.3px; }
  .front-copy { position: absolute; left: 452px; top: 403px; font-size: 18.5px; font-weight: 300; line-height: 22.5px; color: var(--ink-soft); }

  /* back */
  .intro { position: absolute; left: 41px; width: 420px; font-size: 16.5px; font-weight: 300; line-height: 19.5px; color: var(--ink-soft); white-space: nowrap; }
  .intro strong { font-weight: 500; color: var(--ink); }
  .intro .accent { color: var(--green); font-weight: 400; }
  .intro--one { top: 52px; }
  .intro--two { top: 125px; }

  .stamp-area { position: absolute; left: 468px; top: 37px; width: 268px; height: 150px; border: 1px dashed var(--stamp-line); border-radius: 10px; background: #fbfbfb; }

  .services-pill { position: absolute; left: 42px; top: 188px; width: 226px; height: 42px; border-radius: 21px; background: linear-gradient(90deg, var(--pill), var(--pill-end)); display: flex; align-items: center; padding-left: 18px; font-size: 19px; color: var(--ink); letter-spacing: -0.3px; }

  .services { position: absolute; top: 256px; list-style: none; }
  .services--left { left: 42px; }
  .services--right { left: 261px; }
  .services li { display: flex; align-items: center; height: 34px; font-size: 16.5px; font-weight: 400; color: var(--ink-soft); white-space: nowrap; }
  .services svg { width: 18px; height: 18px; margin-right: 8px; flex: none; }
  .services-divider { position: absolute; left: 243px; top: 254px; width: 1px; height: 120px; background: var(--line); }

  .clinic-photo { position: absolute; left: 490px; top: 188px; width: 248px; height: 178px; border: 5px solid #fff; border-radius: 8px; transform: rotate(-6deg); box-shadow: 0 6px 14px rgba(0,0,0,0.18); background: linear-gradient(160deg, #d9e6c4 0%, #9fc9a8 45%, #3fa7a0 70%, #d6a86a 100%); }

  .cta { position: absolute; left: 42px; top: 407px; width: 695px; height: 84px; border: 1.5px solid var(--line); border-radius: 8px; }
  .cta__lead { position: absolute; left: 0; top: 0; width: 374px; height: 100%; background: var(--pill); border-radius: 7px; padding: 16px 0 0 18px; }
  .cta__ask { font-size: 18px; font-weight: 400; line-height: 20px; color: var(--ink); }
  .cta__action { font-size: 24px; font-weight: 500; line-height: 30px; color: var(--ink); letter-spacing: -0.4px; }
  .cta__contact { position: absolute; left: 398px; top: 14px; }
  .contact-line { display: flex; align-items: center; color: var(--ink); white-space: nowrap; }
  .contact-line svg { width: 22px; height: 22px; margin-right: 14px; }
  .contact-line--phone { font-size: 29px; font-weight: 500; height: 34px; letter-spacing: -0.3px; }
  .contact-line--web { font-size: 19px; font-weight: 400; height: 24px; margin-top: 2px; }
</style>
</head>
<body>

<section class="card card--front">
  <div class="smile-art" role="img" aria-label="Cartoon illustration of a big cheerful smile with white teeth"></div>
  <div class="brand">
    <div class="brand__row">
      <span class="brand__dot"></span>
      <span class="brand__name">maple grove</span>
    </div>
    <div class="brand__sub">PEDIATRIC DENTISTRY</div>
  </div>
  <h1 class="headline">Maple Grove</h1>
  <div class="subhead">Pediatric Dentistry</div>
  <div class="tag-pill">Let Your Smile Grow!</div>
  <p class="front-copy">We're committed to creating<br>a fun &amp; gentle dental experience<br>for kids in Fairhaven, CT.</p>
</section>

<section class="card card--back">
  <p class="intro intro--one">Our pediatric dental team specializes in providing<br>high-quality, <strong>compassionate care</strong> in a safe and<br>comfortable environment.</p>
  <p class="intro intro--two">We're dedicated to helping your child develop<br><strong>healthy oral habits</strong> for a lifetime of <span class="accent">beautiful smiles!</span></p>

  <div class="stamp-area"></div>

  <div class="services-pill">Our Featured Services</div>

  <ul class="services services--left">
    <li><svg viewBox="0 0 20 20"><path d="M4 4c2-2 4 0 6 0s4-2 6 0c2 3-1 6-1 9s-1 5-2 5-1-4-3-4-2 4-3 4-2-2-2-5-3-6-1-9z" fill="#4fb86c"/></svg>Dental Cleanings</li>
    <li><svg viewBox="0 0 20 20"><path d="M4 4c2-2 4 0 6 0s4-2 6 0c2 3-1 6-1 9s-1 5-2 5-1-4-3-4-2 4-3 4-2-2-2-5-3-6-1-9z" fill="#4fb86c"/></svg>Pediatric Pulpotomies</li>
    <li><svg viewBox="0 0 20 20"><path d="M4 4c2-2 4 0 6 0s4-2 6 0c2 3-1 6-1 9s-1 5-2 5-1-4-3-4-2 4-3 4-2-2-2-5-3-6-1-9z" fill="#4fb86c"/></svg>Dental Fillings</li>
    <li><svg viewBox="0 0 20 20"><path d="M4 4c2-2 4 0 6 0s4-2 6 0c2 3-1 6-1 9s-1 5-2 5-1-4-3-4-2 4-3 4-2-2-2-5-3-6-1-9z" fill="#4fb86c"/></svg>Dental Crowns</li>
  </ul>
  <div class="services-divider"></div>
  <ul class="services services--right">
    <li><svg viewBox="0 0 20 20"><circle cx="10" cy="10" r="7" fill="none" stroke="#4fb86c" stroke-width="2"/><path d="M7 10l2 2 4-4" fill="none" stroke="#4fb86c" stroke-width="2"/></svg>Restorative Dentistry</li>
    <li><svg viewBox="0 0 20 20"><path d="M7 2h6v5h5v6h-5v5H7v-5H2V7h5z" fill="#4fb86c"/></svg>Pediatric Sedation</li>
    <li><svg viewBox="0 0 20 20"><circle cx="10" cy="10" r="7" fill="none" stroke="#4fb86c" stroke-width="2"/><path d="M7 10l2 2 4-4" fill="none" stroke="#4fb86c" stroke-width="2"/></svg>Preventive Dentistry</li>
    <li><svg viewBox="0 0 20 20"><path d="M7 2h6v5h5v6h-5v5H7v-5H2V7h5z" fill="#4fb86c"/></svg>Pediatric Emergencies</li>
  </ul>

  <div class="clinic-photo" role="img" aria-label="Photo of a bright pediatric treatment room with a teal dental chair and a window"></div>

  <div class="cta">
    <div class="cta__lead">
      <div class="cta__ask">Ready to Grow Roots With Us?</div>
      <div class="cta__action">Book An Appointment Today!</div>
    </div>
    <div class="cta__contact">
      <div class="contact-line contact-line--phone">
        <svg viewBox="0 0 24 24"><path d="M6.6 10.8a15.1 15.1 0 0 0 6.6 6.6l2.2-2.2a1 1 0 0 1 1-.25 11.4 11.4 0 0 0 3.6.57 1 1 0 0 1 1 1V20a1 1 0 0 1-1 1A17 17 0 0 1 3 4a1 1 0 0 1 1-1h3.5a1 1 0 0 1 1 1c0 1.25.2 2.45.57 3.57a1 1 0 0 1-.25 1z" fill="#1e1e1e"/></svg>
        (203) 555-0147
      </div>
      <div class="contact-line contact-line--web">
        <svg viewBox="0 0 24 24"><path d="M9 3a1.5 1.5 0 0 1 3 0v7l5 1.2c1.3.3 2 1.4 1.8 2.7L18 20H9l-4-6 1.3-1.2L9 14z" fill="#1e1e1e"/></svg>
        maplegrovedentistry.com
      </div>
    </div>
  </div>
</section>

</body>
</html>
```